Quarrow Rent and Supply Flyer

A4 flyer to send electronic to potential customer via email to tell them about Quarrow Rent.
We are start up company looking at sending companies a flyer to introduce the business.

No Folds required - just a standard A4 design

Target Market(s)

Concrete and construction companies

Industry/Entity Type

Construction Company

Font styles to use
Sans Serif

Colors
fbee3e

Requirements
Must have
• Quarrow Logo
• Images provided
Nice to have
• Black and Yellow colour scheme
Should not have
• n/a

```html
<!DOCTYPE html>
<html lang="en">
<head>
<meta charset="utf-8">
<title>Quarrow Rent and Supply Flyer</title>
<link href="https://fonts.googleapis.com/css2?family=Oswald:wght@500;700&display=swap" rel="stylesheet">
<style>
  :root {
    --yellow: #f7c21b;
    --black: #0b0b0b;
    --ink: #111111;
    --page-bg: #e9e6e1;
  }
  * { margin: 0; padding: 0; box-sizing: border-box; }
  html, body { width: 1200px; height: 800px; overflow: hidden; }
  body {
    background: var(--page-bg);
    font-family: "Oswald", "Arial Narrow", sans-serif;
    position: relative;
  }
  .flyer {
    position: absolute;
    left: 330px; top: 18px;
    width: 540px; height: 764px;
    background: var(--black);
    overflow: hidden;
    color: var(--yellow);
  }
  .brand {
    position: absolute; top: 26px; left: 0; width: 100%;
    display: flex; justify-content: center; align-items: center; gap: 8px;
  }
  .brand-mark { width: 14px; height: 14px; background: var(--yellow); }
  .brand-name { font-weight: 700; font-size: 20px; letter-spacing: 1px; color: var(--yellow); }

  .title { position: absolute; top: 72px; left: 0; width: 100%; height: 150px; }
  .title svg { position: absolute; inset: 0; }
  .title-line {
    position: absolute; left: 0; width: 100%; text-align: center;
    font-weight: 700; line-height: 1;
  }
  .title-top { top: 12px; font-size: 46px; color: var(--ink); }
  .title-and { top: 67px; font-size: 16px; color: var(--yellow); }
  .title-bottom { top: 94px; font-size: 46px; color: var(--ink); }

  .tagline {
    position: absolute; top: 228px; left: 0; width: 100%;
    text-align: center; font-weight: 700; font-size: 15px; letter-spacing: .3px;
  }
  .equipment-photo {
    position: absolute; top: 256px; left: 30px; width: 480px; height: 172px;
    background: linear-gradient(100deg, #cfcfcf 0%, #8a8a8a 30%, #b3271f 52%, #6b6b6b 72%, #e0601f 90%);
    border-radius: 6px;
  }
  .points { position: absolute; top: 440px; left: 30px; width: 480px; display: flex; gap: 24px; }
  .point { flex: 1; display: flex; gap: 8px; font-size: 12px; font-weight: 500; line-height: 1.25; }
  .point:first-child { margin-top: 18px; }
  .tick { flex: none; width: 16px; height: 14px; margin-top: 1px; }

  .social-band {
    position: absolute; top: 546px; left: 0; width: 100%; height: 22px;
    background: var(--yellow); color: var(--ink);
    font-weight: 700; font-size: 14px; line-height: 22px;
    text-align: right; padding-right: 46px;
  }
  .machine-photo {
    position: absolute; top: 590px; left: 18px; width: 218px; height: 164px;
    background: linear-gradient(160deg, #f0f0f0 0%, #b9b9b9 55%, #5a5a5a 100%);
    border-radius: 6px; z-index: 2;
  }
  .cutter-photo {
    position: absolute; top: 580px; left: 160px; width: 96px; height: 50px;
    background: linear-gradient(90deg, #9a9a9a 0%, #d9661f 100%);
    border-radius: 25px; z-index: 3;
  }
  .contact { position: absolute; top: 578px; left: 270px; width: 260px; }
  .contact-heading { font-weight: 700; font-size: 16px; line-height: 22px; margin-bottom: 2px; }
  .contact-row { display: flex; align-items: center; gap: 10px; font-weight: 700; font-size: 14px; line-height: 20px; }
  .contact-row svg { flex: none; width: 14px; height: 14px; }

  .partner-band {
    position: absolute; top: 692px; left: 0; width: 100%; height: 38px;
    background: var(--yellow);
    display: flex; align-items: center; justify-content: flex-end; gap: 16px; padding-right: 20px;
  }
  .partner { display: flex; align-items: center; gap: 5px; font-weight: 700; font-size: 14px; color: var(--ink); }
  .partner-mark { width: 9px; height: 9px; background: var(--ink); }
</style>
</head>
<body>
  <main class="flyer">
    <header class="brand">
      <span class="brand-mark"></span>
      <span class="brand-name">QUARROW RENT</span>
    </header>

    <section class="title">
      <svg viewBox="0 0 540 150" width="540" height="150" aria-hidden="true">
        <g fill="#f7c21b">
          <rect x="100" y="6" width="340" height="58" rx="4"/>
          <rect x="150" y="88" width="240" height="58" rx="4"/>
          <rect x="60" y="28" width="32" height="4"/>
          <rect x="448" y="22" width="40" height="4"/>
          <rect x="110" y="136" width="32" height="4"/>
          <rect x="398" y="100" width="44" height="4"/>
          <circle cx="80" cy="48" r="3"/>
          <circle cx="460" cy="42" r="3"/>
          <circle cx="130" cy="110" r="3"/>
        </g>
      </svg>
      <div class="title-line title-top">QUARROW RENT</div>
      <div class="title-line title-and">AND</div>
      <div class="title-line title-bottom">SUPPLY</div>
    </section>

    <p class="tagline">CONCRETE, CONSTRUCTION AND COMMUNICATION HIRE EQUIPMENT</p>

    <div class="equipment-photo" role="img" aria-label="Floor grinders, saws and dust extractors lined up in the hire depot"></div>

    <section class="points">
      <div class="point">
        <svg class="tick" viewBox="0 0 16 14"><path d="M1 7l5 5 9-11" fill="none" stroke="#f7c21b" stroke-width="3"/></svg>
        <p>Honing, Polishing, Cutting, Drilling, Demolition and General Hire Equipment Available. Diamond Consumable for sale- core barrels, diamond segments and specialized tooling</p>
      </div>
      <div class="point">
        <svg class="tick" viewBox="0 0 16 14"><path d="M1 7l5 5 9-11" fill="none" stroke="#f7c21b" stroke-width="3"/></svg>
        <p>Good old fashion customer service with over 15 year's experience in the concrete and construction industry. We will BEAT any written quote from our competitors.</p>
      </div>
    </section>

    <div class="social-band">FIND US ON FACEFRAME AND SNAPGRID</div>

    <div class="machine-photo" role="img" aria-label="Concrete floor grinding machine"></div>
    <div class="cutter-photo" role="img" aria-label="Petrol ring saw"></div>

    <section class="contact">
      <p class="contact-heading">CONTACT US:</p>
      <p class="contact-row">
        <svg viewBox="0 0 14 14"><rect x="1" y="3" width="12" height="8" fill="none" stroke="#f7c21b" stroke-width="1.5"/><path d="M1 3l6 5 6-5" fill="none" stroke="#f7c21b" stroke-width="1.5"/></svg>
        info@quarrowrent.com.au
      </p>
      <p class="contact-row">
        <svg viewBox="0 0 14 14"><circle cx="7" cy="7" r="6" fill="none" stroke="#f7c21b" stroke-width="1.5"/><path d="M1 7h12M7 1c-3 3-3 9 0 12M7 1c3 3 3 9 0 12" fill="none" stroke="#f7c21b" stroke-width="1.2"/></svg>
        www.quarrowrent.com.au
      </p>
      <p class="contact-row">
        <svg viewBox="0 0 14 14"><path d="M7 13C3 8 2.5 6.5 2.5 5a4.5 4.5 0 019 0c0 1.5-.5 3-4.5 8z" fill="none" stroke="#f7c21b" stroke-width="1.5"/><circle cx="7" cy="5" r="1.5" fill="#f7c21b"/></svg>
        Unit 4, 12 Dunmore St Kelvale 6071
      </p>
      <p class="contact-row">
        <svg viewBox="0 0 14 14"><path d="M3 1l3 3-1.5 2a8 8 0 003.5 3.5L10 8l3 3-2 2C6 12 2 8 1 3z" fill="#f7c21b"/></svg>
        0491 570 118
      </p>
    </section>

    <footer class="partner-band">
      <span class="partner"><span class="partner-mark"></span>FLINTEDGE</span>
      <span class="partner">BRAVOTEK</span>
      <span class="partner">NORDSAW</span>
      <span class="partner">KELBY</span>
    </footer>
  </main>
</body>
</html>
```